Niche Fitness Rebrand : Q7 Peak Conditioning

We're re-branding our fitness business and need to develop a cleaner, more sophisticated, and sleek website for our clients and potential clients to reference. We're looking to have some photo presence on all pages, with clean, crisp sections for easy reading on the web, and on mobile. We love the BVRdal(.com) website, which represents a very similar target market, and one of the same methods that our business represents. We're looking to take this local studio to a more professional level for future expansion, and need it to be sleek and in line with the growing and competitive marketplace for fitness.
Target Market(s)
70/30 women to men, physically active, upper middle class / professional between the ages of 28-42.
Industry/Entity Type
Fitness
Requirements
Must have
- sleek, professional, high-end design, with easy user navigation.
- About Page - with drop down child pages for management and coaches bios
- Classes Page 'The Methods' - with drop down child pages for different class types
- Location / Schedule Page
- Pricing
- Blog
- Private staff only programming login page
Nice to have
- potential to add an online retail shop -- but not currently necessary.
- Industry websites we like:
- www.bvrdal.example
- www.tarnbrookathletics.example

```html
<!DOCTYPE html>
<html lang="en">
<head>
<meta charset="utf-8">
<title>Q7 Peak Conditioning</title>
<link href="https://fonts.googleapis.com/css2?family=Montserrat:wght@400;600;700;800&family=Open+Sans:ital,wght@0,400;0,600;0,700;1,600&display=swap" rel="stylesheet">
<style>
:root{
  --ink:#0b0b0b;
  --panel:#151515;
  --dark:#1e1e1e;
  --gold:#b48f5f;
  --gold-light:#c9a878;
  --white:#ffffff;
  --muted:#bdbdbd;
  --line:#4a4a4a;
}
*{box-sizing:border-box;margin:0;padding:0}
html,body{width:1200px;height:4813px;overflow:hidden}
body{background:var(--ink);color:var(--white);font-family:"Open Sans",sans-serif;position:relative}
.sec{position:absolute;left:0;width:1200px}
h2.title{font-family:"Montserrat",sans-serif;font-weight:700;font-size:34px;text-align:center;letter-spacing:1px}
.divider{display:block;margin:14px auto 22px;width:120px;height:16px}
.lead{font-size:14px;line-height:22px;text-align:center;color:var(--white);font-weight:600;padding:0 80px}
.photo{display:block}
.topbar{top:0;height:112px;background:#000;display:flex;align-items:center;padding:0 80px}
.brand{display:flex;align-items:center;gap:12px;font-family:"Montserrat",sans-serif;font-weight:700;font-size:26px}
.brand .mark{width:44px;height:44px;border:2px solid var(--white)}
.contacts{margin-left:auto;display:flex;gap:40px}
.contact{display:flex;gap:12px;align-items:center;font-size:14px}
.contact .ic{width:34px;height:34px;background:var(--dark);display:flex;align-items:center;justify-content:center}
.contact b{display:block;font-weight:600}
.nav{top:112px;height:56px;background:rgba(0,0,0,.75);z-index:2;display:flex;align-items:center;padding:0 80px}
.nav a{color:var(--white);text-decoration:none;font-family:"Montserrat",sans-serif;font-size:15px;font-weight:600;flex:1;text-align:center;line-height:50px}
.nav a.on{background:var(--gold)}
.nav a.login{background:var(--gold);flex:0 0 120px}
.hero{top:112px;height:578px;background:radial-gradient(ellipse at 70% 50%,#5a5a5a 0%,#2c2c2c 45%,#0e0e0e 100%)}
.hero h1{position:absolute;left:86px;top:205px;font-family:"Montserrat",sans-serif;font-weight:800;font-size:44px;line-height:58px}
.hero .dots{position:absolute;left:92px;top:380px;display:flex;gap:12px}
.hero .dots i{width:34px;height:5px;background:var(--white)}
.hero .dots i.on{background:var(--gold)}
.welcome{top:690px;height:310px;padding-top:60px}
.welcome p.small{font-size:13px;line-height:21px;text-align:center;color:var(--muted);padding:8px 80px 0}
.mv{top:1000px;height:278px;background:linear-gradient(90deg,#3b3b3b,#242424 50%,#3b3b3b);display:flex;gap:26px;padding:46px 80px}
.mv .box{flex:1;border:1px solid #8a8a8a;background:rgba(0,0,0,.45);text-align:center;padding:38px 40px}
.mv h3{font-family:"Montserrat",sans-serif;font-size:28px;font-weight:700;margin-bottom:14px}
.mv p{font-size:13px;line-height:20px;color:var(--muted)}
.services{top:1278px;height:552px;padding-top:48px}
.cards{display:flex;gap:26px;padding:32px 80px 0}
.card{flex:1;text-align:center}
.card .photo{height:160px;border:3px solid #fff}
.card h4{font-family:"Montserrat",sans-serif;font-size:17px;margin:16px 0 6px}
.card p{font-size:13px;line-height:19px;color:var(--muted)}
.btn{display:inline-block;border:1px solid #fff;font-size:12px;font-weight:700;padding:6px 16px;margin-top:14px}
.video{top:1830px;height:625px;background:linear-gradient(180deg,#4b4b4b,#2f2f2f);padding-top:48px}
.video .screen{position:absolute;left:310px;top:165px;width:590px;height:380px;background:#1a1a1a;border-radius:22px;padding:26px 34px}
.video .screen .photo{width:100%;height:100%;background:linear-gradient(180deg,#d7d2cc,#8c857c)}
.gallery{top:2455px;height:530px;padding-top:48px}
.arrow{position:absolute;top:50%;width:20px;height:40px}
.gal{position:absolute;left:80px;top:130px;width:1040px;height:300px;display:grid;grid-template-columns:310px 1fr 1fr 1fr;grid-template-rows:1fr 1fr;gap:10px}
.gal .feat{grid-row:span 2;border:2px solid #ddd;background:linear-gradient(180deg,#5a5a5a,#2a2a2a);padding:100px 24px 0}
.gal .feat h5{font-size:20px;font-weight:700;text-align:center;margin-bottom:10px}
.gal .feat p{font-size:13px;line-height:19px;text-align:center}
.gal .big{grid-row:span 2}
.blog{top:2985px;height:605px;padding-top:48px}
.posts{display:flex;gap:26px;padding:28px 80px 0}
.post{flex:1;background:#1b1b1b;text-align:center;padding-bottom:18px}
.post .photo{height:180px}
.post h4{font-size:14px;font-weight:700;margin:16px 0 8px}
.post p{font-size:12px;line-height:18px;color:var(--muted);padding:0 24px}
.post .btn{background:var(--gold);border:none;color:#fff}
.testi{top:3590px;height:487px;background:linear-gradient(180deg,#454545,#2a2a2a);padding-top:40px}
.testi blockquote{font-style:italic;font-weight:600;font-size:17px;line-height:27px;text-align:center;padding:20px 140px 0}
.testi .avatar{width:90px;height:90px;border-radius:50%;background:#7a6a5a;margin:16px auto 0;border:3px solid #fff}
.testi .name{text-align:center;font-size:13px;font-weight:700;margin-top:10px}
.testi .tdots{display:flex;justify-content:center;gap:8px;margin-top:14px}
.testi .tdots i{width:22px;height:4px;background:#888}
.testi .tdots i.on{background:var(--white)}
.footer{top:4077px;height:706px;background:linear-gradient(180deg,#2e2e2e,#1a1a1a)}
.quick{position:absolute;left:80px;top:106px;width:1040px;height:118px;background:var(--gold);border-radius:0 0 16px 16px;display:flex}
.quick div{flex:1;text-align:center;padding-top:44px;border-right:1px solid rgba(255,255,255,.4)}
.quick div:last-child{border:none}
.quick h6{font-family:"Montserrat",sans-serif;font-size:16px;font-weight:600}
.quick p{font-size:13px}
.quick small{font-size:10px;opacity:.8}
.qicon{position:absolute;top:-44px;width:90px;height:90px;background:var(--gold);border-radius:50%;display:flex;align-items:center;justify-content:center}
.news{position:absolute;left:80px;top:286px;width:1040px;display:flex;align-items:center;gap:14px;font-size:15px}
.news input{width:300px;height:34px;border:none;padding:0 10px}
.news .sub{background:var(--gold);height:34px;padding:0 14px;line-height:34px;font-size:12px;font-weight:700}
.news .follow{margin-left:auto;display:flex;gap:10px;align-items:center;font-weight:700}
.news .follow i{width:30px;height:30px;border:1px solid #fff;display:block}
.cols{position:absolute;left:80px;top:360px;width:1040px;display:flex;gap:40px;border-top:1px solid var(--line);padding-top:26px}
.cols h6{font-size:16px;font-weight:700;margin-bottom:20px}
.cols ul{list-style:none;font-size:13px;line-height:27px}
.cols input{display:block;width:280px;height:26px;margin-bottom:12px;border:none}
.cols .submit{background:var(--gold);font-size:12px;font-weight:700;padding:6px 16px;display:inline-block}
.cols .det p{font-size:13px;line-height:22px;margin-bottom:12px}
.ghost{position:absolute;right:80px;top:400px;width:170px;height:170px;border:3px solid rgba(255,255,255,.25)}
.copy{top:4783px;height:30px;background:#000;border-top:4px solid #2d6b3a;text-align:center;font-size:12px;line-height:26px}
</style>
</head>
<body>

<header class="sec topbar">
  <div class="brand"><span class="mark"></span>Q7 Peak Conditioning</div>
  <div class="contacts">
    <div class="contact"><span class="ic"><svg width="16" height="16" viewBox="0 0 16 16"><path d="M3 1l3 3-2 2c1 2 3 4 5 5l2-2 3 3-2 3C6 14 2 10 1 3z" fill="#fff"/></svg></span><div><b>Call Us</b>012-555-0147</div></div>
    <div class="contact"><span class="ic"><svg width="18" height="14" viewBox="0 0 18 14"><rect x="1" y="1" width="16" height="12" fill="none" stroke="#fff" stroke-width="1.5"/><path d="M1 1l8 7 8-7" fill="none" stroke="#fff" stroke-width="1.5"/></svg></span><div><b>Mail Us</b>info@q7peak.example</div></div>
  </div>
</header>

<section class="sec hero" role="img" aria-label="Two athletes training on a leg press machine in a smoky gym">
  <h1>CREATE LENGTH.<br>BUILD STRENGTH.</h1>
  <div class="dots"><i class="on"></i><i></i><i></i></div>
</section>
<nav class="sec nav">
  <a class="on">HOME</a><a>ABOUT US</a><a>CLASSES</a><a>LOCATION</a><a>PRICING</a><a>BLOG</a><a class="login">LOGIN</a>
</nav>

<section class="sec welcome">
  <h2 class="title">WELCOME TO Q7 PEAK CONDITIONING</h2>
  <svg class="divider" viewBox="0 0 120 16"><line x1="0" y1="8" x2="50" y2="8" stroke="#666"/><rect x="54" y="2" width="12" height="12" fill="none" stroke="#888"/><line x1="70" y1="8" x2="120" y2="8" stroke="#666"/></svg>
  <p class="lead">Lorem ipsum dolor sit amet, consectetuer adipiscing elit, sed diam nonummy nibh euismod tincidunt ut laoreet dolore magna aliquam erat volutpat. Ut wisi enim ad minim veniam, quis nostrud exerci tation ullamcorper suscipit lobortis nisl ut aliquip ex ea commodo consequat.</p>
  <p class="small">Lorem ipsum dolor sit amet, consectetuer adipiscing elit, sed diam nonummy nibh euismod tincidunt ut laoreet dolore magna aliquam erat volutpat. Ut wisi enim ad minim veniam, quis nostrud exerci tation ullamcorper suscipit lobortis nisl ut aliquip ex ea commodo consequat. Duis autem vel eum iriure dolor in hendrerit in vulputate velit esse molestie consequat, vel illum dolore eu feugiat nulla facilisis at vero eros et accumsan.</p>
</section>

<section class="sec mv" role="img" aria-label="Blurred gym interior behind mission and vision panels">
  <div class="box"><h3>OUR MISSION</h3><p>Lorem ipsum dolor sit amet, consectetuer adipiscing elit, sed diam nonummy nibh euismod tincidunt Lorem ipsum dolor sit amet, consectetuer adipiscing elit, sed diam nonummy</p></div>
  <div class="box"><h3>OUR VISION</h3><p>Lorem ipsum dolor sit amet, consectetuer adipiscing elit, sed diam nonummy nibh euismod tincidunt Lorem ipsum dolor sit amet, consectetuer adipiscing elit, sed diam nonummy</p></div>
</section>

<section class="sec services">
  <h2 class="title">OUR SERVICES</h2>
  <svg class="divider" viewBox="0 0 120 16"><line x1="0" y1="8" x2="50" y2="8" stroke="#666"/><rect x="54" y="2" width="12" height="12" fill="none" stroke="#888"/><line x1="70" y1="8" x2="120" y2="8" stroke="#666"/></svg>
  <p class="lead">Lorem ipsum dolor sit amet, consectetuer adipiscing elit, sed diam nonummy nibh euismod tincidunt ut laoreet dolore magna aliquam erat volutpat. Ut wisi enim ad minim veniam, quis nostrud exerci tation ullamcorper suscipit lobortis nisl ut aliquip ex ea commodo consequat.</p>
  <div class="cards">
    <div class="card"><div class="photo" role="img" aria-label="Class on sliding carriage resistance machines" style="background:linear-gradient(135deg,#6b5a4c,#2f2a26)"></div><h4>LENGTHFORMER</h4><p>Lorem ipsum dolor sit amet,<br>consectetuer adipiscing elit, sed</p><span class="btn">READ MORE</span></div>
    <div class="card"><div class="photo" role="img" aria-label="Athletes on rowing machines" style="background:linear-gradient(135deg,#8a8a8a,#3a3a3a)"></div><h4>ROWING</h4><p>Lorem ipsum dolor sit amet,<br>consectetuer adipiscing elit, sed</p><span class="btn">READ MORE</span></div>
    <div class="card"><div class="photo" role="img" aria-label="Core training in a bright studio" style="background:linear-gradient(135deg,#9aa0a6,#4a4f55)"></div><h4>CORE</h4><p>Lorem ipsum dolor sit amet,<br>consectetuer adipiscing elit, sed</p><span class="btn">READ MORE</span></div>
    <div class="card"><div class="photo" role="img" aria-label="Woman boxing with a heavy bag" style="background:linear-gradient(135deg,#c9b8a6,#2b2b2b)"></div><h4>BOXING</h4><p>Lorem ipsum dolor sit amet,<br>consectetuer adipiscing elit, sed</p><span class="btn">READ MORE</span></div>
  </div>
</section>

<section class="sec video" role="img" aria-label="Hands holding a tablet playing a group fitness class video over a gym backdrop">
  <h2 class="title">WATCH VIDEO</h2>
  <svg class="divider" viewBox="0 0 120 16"><line x1="0" y1="8" x2="50" y2="8" stroke="#888"/><rect x="54" y="2" width="12" height="12" fill="none" stroke="#aaa"/><line x1="70" y1="8" x2="120" y2="8" stroke="#888"/></svg>
  <div class="screen"><div class="photo"></div></div>
</section>

<section class="sec gallery">
  <h2 class="title">OUR GALLERY</h2>
  <svg class="divider" viewBox="0 0 120 16"><line x1="0" y1="8" x2="50" y2="8" stroke="#666"/><rect x="54" y="2" width="12" height="12" fill="none" stroke="#888"/><line x1="70" y1="8" x2="120" y2="8" stroke="#666"/></svg>
  <svg class="arrow" style="left:28px" viewBox="0 0 20 40"><path d="M16 4L4 20l12 16" fill="none" stroke="#999" stroke-width="2"/></svg>
  <svg class="arrow" style="right:28px" viewBox="0 0 20 40"><path d="M4 4l12 16L4 36" fill="none" stroke="#999" stroke-width="2"/></svg>
  <div class="gal">
    <div class="feat" role="img" aria-label="Featured gallery photo of a woman training"><h5>Lorem ipsum dolor</h5><p>Lorem ipsum dolor sit amet, consectetuer adipiscing elit, sed diam nonummy nibh euismod tincidunt ut laoreet dolore magna aliquam erat volutpat.</p></div>
    <div role="img" aria-label="Woman on a rowing machine" style="background:linear-gradient(135deg,#8c8c8c,#3c3c3c)"></div>
    <div role="img" aria-label="Woman stretching on a blue mat" style="background:linear-gradient(135deg,#5fa3c9,#c9a28a)"></div>
    <div class="big" role="img" aria-label="Woman lifting a kettlebell" style="background:linear-gradient(135deg,#a87d63,#3a2c24)"></div>
    <div role="img" aria-label="Athlete training in red light" style="background:linear-gradient(135deg,#7a1f1f,#2a1010)"></div>
    <div role="img" aria-label="Man holding weights" style="background:linear-gradient(135deg,#6f5f52,#251e19)"></div>
  </div>
</section>

<section class="sec blog">
  <h2 class="title">LATEST BLOG POSTS</h2>
  <svg class="divider" viewBox="0 0 120 16"><line x1="0" y1="8" x2="50" y2="8" stroke="#666"/><rect x="54" y="2" width="12" height="12" fill="none" stroke="#888"/><line x1="70" y1="8" x2="120" y2="8" stroke="#666"/></svg>
  <p class="lead">Lorem ipsum dolor sit amet, consectetuer adipiscing elit, sed diam nonummy nibh euismod tincidunt ut laoreet dolore magna aliquam erat volutpat. Ut wisi enim ad minim veniam, quis nostrud exerci tation ullamcorper suscipit lobortis nisl ut aliquip ex ea commodo</p>
  <svg class="arrow" style="left:28px;top:340px" viewBox="0 0 20 40"><path d="M16 4L4 20l12 16" fill="none" stroke="#999" stroke-width="2"/></svg>
  <svg class="arrow" style="right:28px;top:340px" viewBox="0 0 20 40"><path d="M4 4l12 16L4 36" fill="none" stroke="#999" stroke-width="2"/></svg>
  <div class="posts">
    <div class="post"><div class="photo" role="img" aria-label="Two people lifting dumbbells" style="background:linear-gradient(135deg,#7f8a94,#2c3238)"></div><h4>LOREM IPSUM DOLOR SIT AMET</h4><p>Lorem ipsum dolor sit amet, consectetuer adipiscing elit, sed diam nonummy nibh euismod. Tincidunt euismod and a data been done.</p><span class="btn">Read More</span></div>
    <div class="post"><div class="photo" role="img" aria-label="Group stretching class" style="background:linear-gradient(135deg,#c4c8cc,#6a7078)"></div><h4>LOREM IPSUM DOLOR SIT AMET</h4><p>Lorem ipsum dolor sit amet, consectetuer adipiscing elit, sed diam nonummy nibh euismod. Tincidunt euismod and a data been done.</p><span class="btn">Read More</span></div>
    <div class="post"><div class="photo" role="img" aria-label="Trainer assisting a client" style="background:linear-gradient(135deg,#9a8f86,#3f3833)"></div><h4>LOREM IPSUM DOLOR SIT AMET</h4><p>Lorem ipsum dolor sit amet, consectetuer adipiscing elit, sed diam nonummy nibh euismod. Tincidunt euismod and a data been done.</p><span class="btn">Read More</span></div>
  </div>
</section>

<section class="sec testi" role="img" aria-label="Blurred fitness studio behind client testimonials">
  <h2 class="title">CLIENT TESTIMONIALS</h2>
  <blockquote>Lorem ipsum dolor sit amet, consectetuer adipiscing elit, sed diam nonummy nibh euismod tincidunt ut laoreet dolore magna aliquam erat volutpat. Ut wisi enim ad minim veniam, quis nostrud exerci tation ullamcorper suscipit</blockquote>
  <div class="avatar" role="img" aria-label="Client portrait"></div>
  <p class="name">LOREM IPSUM DOLOR</p>
  <div class="tdots"><i class="on"></i><i></i><i></i></div>
</section>

<footer class="sec footer">
  <div class="quick">
    <div style="position:relative"><span class="qicon" style="left:125px"><svg width="30" height="30" viewBox="0 0 16 16"><path d="M3 1l3 3-2 2c1 2 3 4 5 5l2-2 3 3-2 3C6 14 2 10 1 3z" fill="#fff"/></svg></span><h6>QUICK CONTACT</h6><p>012-555-0147</p><small>support@q7peak.example</small></div>
    <div style="position:relative"><span class="qicon" style="left:125px"><svg width="30" height="30" viewBox="0 0 20 20"><path d="M2 9h4v9H2zM7 9l4-7c2 0 2 2 1 5h5c1 0 2 1 1 3l-2 7H7z" fill="#fff"/></svg></span><h6>DISCOUNT</h6><p>50% OFF FOR 1 YEAR</p><small>Ut wisi enim ad minim veniam</small></div>
    <div style="position:relative"><span class="qicon" style="left:125px"><svg width="30" height="30" viewBox="0 0 20 20"><circle cx="10" cy="10" r="8" fill="none" stroke="#fff" stroke-width="2"/><path d="M6 10l3 3 5-6" fill="none" stroke="#fff" stroke-width="2"/></svg></span><h6>SATISFACTION</h6><p>100% MONEY BACK GUARANTEE</p><small>Ut wisi enim ad minim veniam</small></div>
  </div>
  <div class="news">
    <svg width="26" height="20" viewBox="0 0 18 14"><rect x="1" y="1" width="16" height="12" fill="none" stroke="#fff" stroke-width="1.5"/><path d="M1 1l8 7 8-7" fill="none" stroke="#fff" stroke-width="1.5"/></svg>
    <span>Newsletter Signup</span><input placeholder="Enter your email here"><span class="sub">SUBSCRIBE</span>
    <div class="follow">Follow Us <i></i><i></i><i></i><i></i></div>
  </div>
  <div class="cols">
    <div style="width:200px"><h6>Quick Links</h6><ul><li>› Home</li><li>› About Us</li><li>› Classes</li><li>› Location</li><li>› Pricing</li><li>› Blog</li></ul></div>
    <div style="width:320px"><h6>QUICK INQUIRY</h6><input placeholder=" Name"><input placeholder=" Phone"><input placeholder=" Email Address"><input placeholder=" Message"><span class="submit">SUBMIT</span></div>
    <div class="det"><h6>CONTACT DETAILS</h6><p>RIDGELINE STUDIO HALL<br>Lorem ipsum dolor sit amet, conse<br>tetuer adipiscing elit, sed</p><p>012-555-0147</p><p>info@q7peak.example</p></div>
  </div>
  <div class="ghost"></div>
</footer>
<div class="sec copy">Copyright 2017 Q7 Peak Conditioning | All Right Reserved</div>

</body>
</html>
```